Stationary Design for Medical Distribution Company

We are a Medical Distribution Company based in Dar es salaam, Tanzania (East Africa). Our company was established in 1995 and we are a reputed and respected Pharmaceuticals and Medical Supplies company in the region.
We have just recently changed our company logo. A new company logo has just recently been selected through Pixel Harbor and we are now looking for stationary designs such as Business Cards, Letterheads, Envelopes, etc.. for our company.
We request you all to take a look at the attached new company logo and give us your best possible designs.
We would prefer to have a double sided business card. For letterheads, we are open to your ideas/designs.
We are looking forward for your designs!
Updates
Company details to be incorporated in designs:
Company Name: KOVEL PHARMACEUTICALS LIMITED
Company Address: Office # 42, Tumaini Works Ltd., Msasani Lane, Dar es salaam, Tanzania
Tel: +255 22 2917348 / 49, Fax: +255 22 2917350
Email: info@kovelmedix.example
Website: www.kovelmedix.example
Also should include Cell number +255 XXX XXX XXX
Name and Designation.....
Target Market(s)
Medical Sector
Industry/Entity Type
Medical
Look and feel

```html
<!DOCTYPE html>
<html lang="en">
<head>
<meta charset="utf-8">
<title>Kovel Pharmaceuticals Limited – Envelope</title>
<link rel="stylesheet" href="https://fonts.googleapis.com/css2?family=Open+Sans:wght@400&family=Oswald:wght@600&family=Tinos&display=swap">
<style>
  :root {
    --paper: #ffffff;
    --brand-red: #c63d3f;
    --frame-pink: #f4dede;
    --wash-pink: #fbeeee;
    --name-grey: #3b3536;
    --ink: #111111;
  }
  * { margin: 0; padding: 0; box-sizing: border-box; }
  html, body {
    width: 1200px;
    height: 600px;
    overflow: hidden;
    background: var(--paper);
  }
  .envelope {
    position: relative;
    width: 1200px;
    height: 600px;
    background: var(--paper);
  }
  .return-block {
    position: absolute;
    left: 69px;
    top: 68px;
    width: 404px;
    height: 277px;
    border: 9px solid var(--frame-pink);
  }
  .return-wash {
    position: absolute;
    inset: 0;
    background: linear-gradient(135deg, var(--wash-pink) 0%, var(--paper) 45%, var(--wash-pink) 75%, var(--paper) 100%);
  }
  .brand-square {
    position: absolute;
    left: 5px;
    top: 5px;
    width: 106px;
    height: 106px;
    border-radius: 10px;
    background: var(--brand-red);
  }
  .brand-name {
    position: absolute;
    left: 116px;
    top: 8px;
    font-family: "Open Sans", sans-serif;
    font-weight: 400;
    font-size: 32px;
    line-height: 34.4px;
    color: var(--name-grey);
    letter-spacing: -0.2px;
    white-space: nowrap;
  }
  .sender-address {
    position: absolute;
    left: 121px;
    top: 117px;
    font-family: "Oswald", sans-serif;
    font-weight: 600;
    font-size: 19px;
    line-height: 25.6px;
    color: var(--ink);
    font-style: normal;
    letter-spacing: 0.4px;
    white-space: nowrap;
  }
  .recipient-address {
    position: absolute;
    left: 545px;
    top: 280px;
    font-family: "Tinos", serif;
    font-size: 21px;
    line-height: 26.4px;
    color: var(--ink);
    font-style: normal;
    white-space: nowrap;
  }
</style>
</head>
<body>
  <main class="envelope">
    <section class="return-block">
      <div class="return-wash" role="img" aria-label="Faint pink decorative background pattern behind the sender block"></div>
      <div class="brand-square"></div>
      <div class="brand-name">Kovel<br>Pharmaceuticals<br>Limited</div>
      <address class="sender-address">
        Office #42<br>
        Tumaini Works Ltd.<br>
        Msasani Lane<br>
        Dar es salaam<br>
        Tanzania
      </address>
    </section>
    <address class="recipient-address">
      Delia Marsh<br>
      1520 Orchard Lane<br>
      Fairbrook, SC 29301
    </address>
  </main>
</body>
</html>
```